Organic Food Packaging for Bulk Nuts, Seeds, Dried fruit

We need a simple yet creative packaging design for our kelpvane brand. The packaging will be for stand up bags. We would like a very simply design that we can use for all of our packaging needs. The size of the pouch is 6" wide by 12" tall. You can visit our site. www.kelpvane.example to get some ideas. Here are some packaging ideas we do like. https://boxes.makerloft.example/contest/5092714https://artmarket.example/item/dry-fuits-bag-packaging/20471935

Target Market(s)

organic foods, health food, green, speciality and gourmet shops

Industry/Entity Type

Food Production

Font styles to use
Sans Serif

Requirements
Must have
• We need space in the middle of the pouch to be white so we can apply labels on it.
Nice to have
• Simple vines, leaves, gray patterns, 2-3 color design will be best. We would like a see through window. I have attached our logo.
Should not have
• many colors or lots of background colors.

```html
<!DOCTYPE html>
<html lang="en">
<head>
<meta charset="utf-8">
<title>kelpvane stand-up pouch – 12x6″ colour options</title>
<link href="https://fonts.googleapis.com/css2?family=Arimo:wght@400;500&display=swap" rel="stylesheet">
<style>
  :root {
    --canvas: #ffffff;
    --spec-pink: #e8308a;
    --pouch-cream: #fefcf0;
    --pouch-mist: #f0f5f5;
    --frame-gray: #5f6360;
    --frame-green: #5b7c45;
    --brand-green: #74a862;
    --label-white: #ffffff;
    --leaf-light: #b9d27a;
    --leaf-mid: #8fb45a;
    --leaf-deep: #5f8c3c;
  }
  html, body {
    margin: 0;
    padding: 0;
    width: 1162px;
    height: 1200px;
    overflow: hidden;
    background: var(--canvas);
  }
  .sheet {
    display: block;
    width: 1162px;
    height: 1200px;
    font-family: "Arimo", Arial, sans-serif;
  }
  .size-note, .option-number, .zone-note {
    fill: var(--spec-pink);
    font-family: "Arimo", Arial, sans-serif;
  }
  .size-note { font-size: 46px; }
  .option-number { font-size: 64px; }
  .zone-note { font-size: 31px; }
  .pouch-outline {
    stroke: url(#frameShade);
    stroke-width: 18;
    stroke-linejoin: round;
  }
  .pouch--cream .pouch-outline { fill: var(--pouch-cream); }
  .pouch--mist .pouch-outline { fill: var(--pouch-mist); }
  .brand-name {
    fill: var(--brand-green);
    font-family: "Arimo", Arial, sans-serif;
    font-weight: 500;
    font-size: 92px;
    letter-spacing: 4px;
  }
  .brand-dot { fill: var(--brand-green); }
  .label-zone {
    fill: var(--label-white);
    stroke: var(--spec-pink);
    stroke-width: 1;
  }
  .window-zone {
    fill: var(--label-white);
    stroke: var(--frame-gray);
    stroke-width: 11;
  }
</style>
</head>
<body>
<svg class="sheet" viewBox="0 0 1450 1500" xmlns="http://www.w3.org/2000/svg">
  <defs>
    <linearGradient id="frameShade" gradientUnits="userSpaceOnUse" x1="0" y1="60" x2="0" y2="1360">
      <stop offset="0" stop-color="#646464"/>
      <stop offset="0.2" stop-color="#5b7c45"/>
      <stop offset="0.75" stop-color="#5b7c45"/>
      <stop offset="1" stop-color="#5f6360"/>
    </linearGradient>
    <linearGradient id="foliageTone" x1="0" y1="0" x2="0" y2="1">
      <stop offset="0" stop-color="#b9d27a" stop-opacity="0.55"/>
      <stop offset="0.35" stop-color="#8fb45a"/>
      <stop offset="1" stop-color="#5f8c3c"/>
    </linearGradient>
    <clipPath id="pouchInside">
      <path d="M50 75 H682 V178 Q670 190 682 205 L628 1300 L595 1345 Q370 1360 140 1345 L112 1300 L50 205 Q62 190 50 178 Z"/>
    </clipPath>
  </defs>

  <text class="size-note" x="730" y="50" text-anchor="middle">12x6”</text>

  <g class="pouch pouch--cream">
    <path class="pouch-outline" d="M50 75 H682 V178 Q670 190 682 205 L628 1300 L595 1345 Q370 1360 140 1345 L112 1300 L50 205 Q62 190 50 178 Z"/>
    <g class="brand-mark">
      <circle class="brand-dot" cx="140" cy="414" r="22"/>
      <text class="brand-name" x="185" y="446">kelpvane</text>
    </g>
    <rect class="label-zone" x="180" y="631" width="371" height="179"/>
    <text class="zone-note" x="366" y="729" text-anchor="middle">For Label</text>
    <rect class="window-zone" x="140" y="848" width="452" height="222" rx="24"/>
    <text class="zone-note" x="388" y="960" text-anchor="middle">Transparent</text>
    <text class="zone-note" x="388" y="1001" text-anchor="middle">Window</text>
    <rect class="foliage" x="100" y="1076" width="540" height="280" fill="url(#foliageTone)" clip-path="url(#pouchInside)" role="img" aria-label="Watercolour band of trailing green vines and leaves along the bottom of the pouch"/>
    <text class="option-number" x="362" y="1434" text-anchor="middle">1</text>
  </g>

  <g class="pouch pouch--mist" transform="translate(722 0)">
    <path class="pouch-outline" d="M50 75 H682 V178 Q670 190 682 205 L628 1300 L595 1345 Q370 1360 140 1345 L112 1300 L50 205 Q62 190 50 178 Z"/>
    <g class="brand-mark">
      <circle class="brand-dot" cx="140" cy="414" r="22"/>
      <text class="brand-name" x="185" y="446">kelpvane</text>
    </g>
    <rect class="label-zone" x="180" y="631" width="371" height="179"/>
    <rect class="window-zone" x="140" y="848" width="452" height="222" rx="24"/>
    <rect class="foliage" x="100" y="1076" width="540" height="280" fill="url(#foliageTone)" clip-path="url(#pouchInside)" role="img" aria-label="Watercolour band of trailing green vines and leaves along the bottom of the pouch"/>
    <text class="option-number" x="425" y="1434" text-anchor="middle">2</text>
  </g>
</svg>
</body>
</html>
```